Stationary Design Letterhead and Envelope

Artist should provide Letterhead and envelop stationary designs

Info for stationary:
Fenwarde Outdoor Advertising
4857 Mesa Rd. 318 N. PO BOX 582917
Austin, TX 78651

Dale Fenwarde
President
512-608-2917
dale@fenwardeoutdoor.example
fenwardeoutdoor.example

Target Market(s)

clients

Colors
0054AA
0677BA
7BADD7
CADEEF
E8F1F8

Requirements
Must have
• high quality unique eye catching and dynamic

```html
<!DOCTYPE html>
<html lang="en">
<head>
<meta charset="utf-8">
<title>Fenwarde Outdoor Advertising — Stationery</title>
<link rel="stylesheet" href="https://fonts.googleapis.com/css2?family=Nunito+Sans:wght@400;600;800&family=Source+Sans+3:wght@400;600&display=swap">
<style>
  :root {
    --backdrop: #e4e4e5;
    --paper: #f6f6f6;
    --paper-edge: #e2e2e2;
    --ink: #0b0b0c;
    --text: #333;
    --brand-blue: #0b67a8;
    --blue-dark: #0054AA;
    --fold: #d9d9d9;
  }
  * { margin: 0; padding: 0; box-sizing: border-box; }
  html, body { width: 1200px; height: 952px; overflow: hidden; }
  body {
    background: var(--backdrop);
    font-family: "Nunito Sans", sans-serif;
    color: var(--text);
    position: relative;
  }

  /* Letterhead */
  .letterhead {
    position: absolute;
    left: 429px; top: 100px;
    width: 505px; height: 696px;
    background: var(--paper);
    box-shadow: 0 2px 6px rgba(0,0,0,.12);
  }
  .letterhead .art { position: absolute; inset: 0; }
  .wordmark {
    position: absolute;
    display: flex; align-items: center; gap: 8px;
    font-family: "Nunito Sans", sans-serif;
    font-weight: 800;
    color: var(--ink);
    text-transform: uppercase;
    line-height: 1.05;
  }
  .wordmark .mark-square { background: var(--brand-blue); flex: none; }
  .letterhead .wordmark { left: 20px; top: 48px; font-size: 15px; width: 190px; }
  .letterhead .wordmark .mark-square { width: 30px; height: 30px; }

  .contact {
    position: absolute; left: 292px; top: 28px; width: 200px;
    font-size: 11.5px;
  }
  .contact .line { display: flex; align-items: center; gap: 7px; height: 16px; color: #444; font-weight: 400; }
  .contact svg { width: 10px; height: 10px; flex: none; }
  .contact .rule { border-top: 1.2px solid var(--ink); width: 150px; margin: 6px 0 5px; }
  .contact .company { font-size: 10.5px; font-weight: 600; color: var(--ink); text-transform: uppercase; }
  .contact .company .accent { color: var(--brand-blue); }
  .contact .address { font-family: "Source Sans 3", sans-serif; font-size: 10.5px; line-height: 15px; color: #333; }

  .signatory { position: absolute; left: 292px; top: 624px; }
  .signatory .name { font-size: 14px; font-weight: 600; color: var(--brand-blue); text-transform: uppercase; line-height: 16px; }
  .signatory .role { font-size: 12px; color: #444; line-height: 16px; }

  .web {
    position: absolute; color: #fff; font-size: 11.5px; font-weight: 400; white-space: nowrap;
  }
  .web .accent { color: #2f8fd6; }
  .letterhead .web {
    left: 262px; width: 140px; text-align: right;
    top: 669px; font-size: 11px; line-height: 14px;
  }

  /* Envelope */
  .envelope {
    position: absolute;
    left: 96px; top: 301px;
    width: 471px; height: 331px;
    background: var(--paper);
    box-shadow: 0 6px 18px rgba(0,0,0,.18);
  }
  .envelope .art { position: absolute; inset: 0; }
  .envelope .wordmark { left: 150px; top: 52px; font-size: 13px; width: 180px; }
  .envelope .wordmark .mark-square { width: 26px; height: 26px; }
  .envelope .web { left: 0; width: 401px; text-align: center; top: 140px; font-size: 10px; }
</style>
</head>
<body>

<section class="letterhead" aria-label="Letterhead">
  <svg class="art" viewBox="0 0 505 696" width="505" height="696" aria-hidden="true">
    <line x1="5" y1="6" x2="470" y2="685" stroke="var(--fold)" stroke-width="1.2"/>
    <polygon points="0,665 431,665 414,690 0,690" fill="var(--ink)"/>
    <polygon points="416,696 451,661 486,696" fill="var(--ink)"/>
    <polygon points="455,643 505,591 505,696" fill="var(--brand-blue)"/>
  </svg>

  <div class="wordmark"><span class="mark-square"></span><span>Fenwarde Outdoor Advertising</span></div>

  <div class="contact">
    <div class="line">
      <svg viewBox="0 0 24 24" fill="none" stroke="#444" stroke-width="2"><path d="M5 3h4l2 5-3 2a11 11 0 0 0 6 6l2-3 5 2v4a2 2 0 0 1-2 2A17 17 0 0 1 3 5a2 2 0 0 1 2-2z"/></svg>
      <span>512-608-2917</span>
    </div>
    <div class="line">
      <svg viewBox="0 0 24 24" fill="none" stroke="#444" stroke-width="2"><rect x="3" y="5" width="18" height="14"/><path d="M3 6l9 7 9-7"/></svg>
      <span>dale@fenwardeoutdoor.example</span>
    </div>
    <div class="rule"></div>
    <div class="company"><span class="accent">Fen</span>warde Outdoor Advertising</div>
    <div class="address">4857 Mesa Rd. 318 N. PO BOX 582917<br>Austin, TX 78651</div>
  </div>

  <div class="signatory">
    <div class="name">Dale Fenwarde</div>
    <div class="role">President</div>
  </div>

  <div class="web"><span class="accent">fen</span>wardeoutdoor.example</div>
</section>

<section class="envelope" aria-label="Envelope">
  <svg class="art" viewBox="0 0 471 331" width="471" height="331" aria-hidden="true">
    <polyline points="0,10 12,165 459,165 471,10" fill="none" stroke="var(--paper-edge)" stroke-width="1"/>
    <line x1="12" y1="172" x2="2" y2="310" stroke="var(--paper-edge)" stroke-width="1"/>
    <line x1="459" y1="172" x2="469" y2="310" stroke="var(--paper-edge)" stroke-width="1"/>
    <polygon points="12,137 401,137 383,159 13,159" fill="var(--ink)"/>
    <polygon points="389,165 421,132 455,165" fill="var(--ink)"/>
    <polygon points="424,119 463,79 456,150" fill="var(--brand-blue)"/>
  </svg>

  <div class="wordmark"><span class="mark-square"></span><span>Fenwarde Outdoor Advertising</span></div>

  <div class="web"><span class="accent">fen</span>wardeoutdoor.example</div>
</section>

</body>
</html>
```